Law Firm Website (Designed in Wix)

A website designed using my Wix account.
A website for a generalist law firm based in Melbourne, Australia.
The areas of practice include:
Criminal Law
Family Law
Civil Litigation
Wills & Probate
PELIX Claims
The colour theme will be green, black and white.
Website will require the following elements:
1. Chat box
2. General Description of the practice
3. Practice Areas (for selection)
4. Calendar bookings for Microsoft Outlook
5. Email enquiries
6. Telephone enquiries
7. Business location map
8. Videos
9. Photos

The following website can be used as inspiration, however I am looking for a copy and paste version of this site:
brunhollowadvocates.com

Target Market(s)

People requiring a Lawyer for Criminal, Family, Wills and Probabte, Conveyancing and Civil Litigstion Matters

Industry/Entity Type

Legal Sector

Coding

Coded - Design and coding required

Number of Pages Required

5+ page

Font styles to use
Other font styles liked:
• Based on business card

Requirements
Must have
• Colours and theme based on business card

```html
<!DOCTYPE html>
<html lang="en">
<head>
<meta charset="utf-8">
<title>Greenvale Lawyers</title>
<link href="https://fonts.googleapis.com/css2?family=Poppins:wght@400;500;600;700&display=swap" rel="stylesheet">
<style>
:root{
  --green:#1b7a2c;
  --green-dark:#0d5a19;
  --green-deep:#0a3f12;
  --ink:#1d1d1d;
  --text:#333;
  --muted:#6b6b6b;
  --mist:#eef4fa;
  --white:#fff;
  --night:#202020;
}
*{box-sizing:border-box;margin:0;padding:0}
html,body{width:1200px;height:5098px;overflow:hidden}
body{position:relative;font-family:'Poppins',sans-serif;color:var(--text);background:var(--white)}
.abs{position:absolute}
.btn{position:absolute;display:flex;align-items:center;justify-content:center;border-radius:30px;font-size:11px;font-weight:600;text-transform:uppercase;letter-spacing:.3px;white-space:nowrap}
.btn-solid{background:var(--green);color:var(--white)}
.btn-white{background:var(--white);color:var(--green-dark)}
.btn-outline{border:2px solid var(--green);color:var(--green-dark);background:transparent}
.brand{display:flex;align-items:center;gap:8px;color:var(--green-dark);font-weight:600;font-size:22px;line-height:1;letter-spacing:.5px;white-space:nowrap}
.brand-dot{flex:none;width:26px;height:26px;border-radius:50%;background:var(--green)}
.h2{position:absolute;left:0;width:1200px;text-align:center;font-size:28px;font-weight:500;color:var(--ink)}
.ticks{list-style:none}
.ticks li{position:relative;padding-left:23px;font-size:13px;line-height:18px;color:var(--ink)}
.ticks li svg{position:absolute;left:0;top:2px}
.site-header{position:absolute;top:0;left:0;width:1200px;height:70px;background:var(--white)}
.site-header .brand{position:absolute;left:138px;top:20px}
.nav{position:absolute;left:477px;top:29px;display:flex;gap:30px;font-size:11px;font-weight:500;color:var(--ink);text-transform:uppercase}
.hero{position:absolute;top:70px;left:0;width:1200px;height:620px}
.hero svg{position:absolute;left:0;top:0}
.hero-title{position:absolute;left:168px;top:150px;color:var(--white);font-size:36px;font-weight:500;line-height:50px;text-transform:uppercase}
.hero-text{position:absolute;left:168px;top:258px;width:380px;color:var(--white);font-size:14.5px;line-height:26px}
.about-lead{position:absolute;left:182px;top:794px;width:836px;text-align:center;font-size:14.5px;line-height:26px;font-weight:500;color:var(--ink)}
.about-body{position:absolute;left:162px;top:914px;width:440px;font-size:14px;line-height:21px;color:var(--ink)}
.find-title{position:absolute;left:644px;top:1400px;font-size:24px;font-weight:500;color:var(--ink)}
.find-text{position:absolute;left:644px;top:1440px;width:420px;font-size:11.5px;line-height:21px;color:var(--muted)}
.steps{position:absolute;top:1838px;left:0;width:1200px;height:538px;background:var(--mist)}
.step{position:absolute;top:138px;width:260px;height:254px;background:var(--white);border:1px solid #dde3ea;box-shadow:0 2px 6px rgba(0,0,0,.06);text-align:center}
.step-icon{width:62px;height:62px;border-radius:50%;background:var(--green);margin:32px auto 0;display:flex;align-items:center;justify-content:center}
.step-no{margin-top:30px;font-size:10px;font-weight:600;color:var(--green)}
.step h3{font-size:17px;font-weight:600;color:var(--ink);margin-top:4px}
.step p{width:222px;margin:10px auto 0;font-size:11.5px;line-height:20px;color:var(--muted)}
.voices{position:absolute;top:2376px;left:0;width:1200px;height:471px;background:linear-gradient(180deg,var(--green) 0%,var(--green-dark) 100%);overflow:hidden}
.voice{position:absolute;top:204px;width:420px;height:164px;background:var(--white);text-align:center;padding-top:36px}
.voice p{font-size:13px;line-height:26px;color:var(--muted);width:340px;margin:0 auto}
.voice strong{display:block;margin-top:8px;font-size:13px;font-weight:600;color:var(--ink)}
.avatar{position:absolute;top:150px;width:76px;height:76px;border-radius:50%;background:linear-gradient(160deg,#8b96a3,#2e3843);border:3px solid var(--white)}
.dots{position:absolute;display:flex;gap:5px}
.dots span{width:12px;height:12px;border-radius:50%;background:var(--white)}
.practice{position:absolute;top:2960px;left:0;width:1200px;height:390px;overflow:hidden}
.area{position:absolute;top:0;width:324px;height:390px;background:var(--white);box-shadow:0 2px 10px rgba(0,0,0,.1);text-align:center}
.area-photo{height:184px}
.area h3{margin-top:22px;font-size:19px;font-weight:500;color:var(--ink)}
.area p{width:270px;margin:8px auto 0;font-size:13.5px;line-height:21px;color:var(--text)}
.area .btn{position:relative;width:112px;height:30px;margin:14px auto 0;font-size:10.5px}
.gallery-band{position:absolute;top:3495px;left:0;width:1200px;height:475px;background:var(--mist)}
.gallery{position:absolute;top:3608px;left:0;width:1200px;height:279px;display:flex}
.gallery div{flex:1;position:relative}
.message{position:absolute;left:255px;top:4045px;width:712px;height:548px;background:linear-gradient(180deg,var(--green) 0%,var(--green-deep) 100%);border-radius:0 90px 0 0}
.message h2{position:absolute;left:0;top:36px;width:712px;text-align:center;color:var(--white);font-size:27px;font-weight:500}
.field{position:absolute;left:78px;width:558px;height:50px;background:var(--white);font-size:12px;color:var(--ink);padding:16px 0 0 20px}
.footer{position:absolute;top:4560px;left:0;width:1200px;height:538px}
.footer svg.bg{position:absolute;left:0;top:0}
.news-title{position:absolute;left:0;top:58px;width:1200px;text-align:center;color:var(--white);font-size:16px;font-weight:600}
.news-input{position:absolute;left:360px;top:101px;width:500px;height:36px;border:1px solid rgba(255,255,255,.7);border-radius:20px;color:rgba(255,255,255,.75);font-size:11px;padding:10px 0 0 20px}
.news-btn{left:690px;top:101px;width:170px;height:36px}
.f-col{position:absolute;top:195px;color:var(--white)}
.f-col h4{font-size:14px;font-weight:500;text-transform:uppercase;margin-bottom:16px}
.f-col ul{list-style:none;font-size:11.5px;line-height:26px}
.f-item{position:relative;padding-left:38px;font-size:11.5px;line-height:17px;margin-bottom:14px;white-space:nowrap}
.f-item i{position:absolute;left:0;top:2px;width:28px;height:28px;border-radius:50%;background:var(--white);display:flex;align-items:center;justify-content:center}
.social{display:flex;gap:12px;margin-top:18px}
.social span{width:28px;height:28px;border-radius:50%;background:var(--white)}
.copyright{position:absolute;left:0;bottom:0;width:1200px;height:58px;background:var(--night);color:var(--white);font-size:11px;text-align:center;padding-top:22px}
</style>
</head>
<body>

<header class="site-header">
  <div class="brand"><span class="brand-dot"></span>GREENVALE LAWYERS</div>
  <nav class="nav"><span>About Us</span><span>Lawyers</span><span>Pratice Areas</span><span>Cases</span></nav>
  <span class="btn btn-solid" style="left:917px;top:22px;width:142px;height:33px">Contact Us</span>
</header>

<section class="hero">
  <svg width="1200" height="620" viewBox="0 0 1200 620">
    <defs>
      <linearGradient id="heroGreen" x1="0" y1="0" x2="1" y2="1">
        <stop offset="0" stop-color="#1f8a33"/><stop offset="1" stop-color="#0b5417"/>
      </linearGradient>
      <linearGradient id="heroPhoto" x1="0" y1="0" x2="1" y2="1">
        <stop offset="0" stop-color="#a0735a"/><stop offset=".45" stop-color="#5b4a42"/><stop offset="1" stop-color="#1e2228"/>
      </linearGradient>
    </defs>
    <polygon points="0,0 1200,0 1200,525 870,585 0,480" fill="url(#heroGreen)"/>
    <circle cx="210" cy="160" r="110" fill="#0f5f1d" opacity=".55"/>
    <polygon points="0,480 870,585 870,600 0,505" fill="#202020"/>
    <polygon role="img" aria-label="Photo of two smiling lawyers in dark suits, one holding a clipboard" points="610,0 1200,0 1200,525 870,585 575,545" fill="url(#heroPhoto)"/>
  </svg>
  <h1 class="hero-title">Welcome to<br>Greenvale Lawyers</h1>
  <p class="hero-text">Lorem Ipsum has been the industry's standard dummy text ever since the 1500s, when an un-</p>
  <span class="btn btn-white" style="left:158px;top:326px;width:173px;height:40px">Message Us</span>
</section>

<h2 class="h2" style="top:742px">About Us</h2>
<p class="about-lead">Lorem Ipsum has been the industry's standard dummy text ever since the 1500s, when an unknown print-er took a galley of type and scrambled it to make a type specimen book.</p>
<p class="about-body">The industry's standard dummy text ever since the 1500s. when an unknown printer took a galley of type and scrambled it to make a type specimen book. It has survived not only five centuries, but also the leap into electronic typesetting, remaining essentially unchanged. It was popularised in the 1960s</p>
<ul class="ticks abs" style="left:162px;top:1060px;width:380px">
  <li style="margin-bottom:14px"><svg width="15" height="15" viewBox="0 0 15 15"><circle cx="7.5" cy="7.5" r="7.5" fill="#1b7a2c"/><path d="M4 7.7l2.3 2.3L11 5.3" stroke="#fff" stroke-width="1.6" fill="none"/></svg>The industry's standard dummy text ever since the 1500s. when an unknown.</li>
  <li><svg width="15" height="15" viewBox="0 0 15 15"><circle cx="7.5" cy="7.5" r="7.5" fill="#1b7a2c"/><path d="M4 7.7l2.3 2.3L11 5.3" stroke="#fff" stroke-width="1.6" fill="none"/></svg>The industry's standard dummy text ever since the 1500s. when an unknown.</li>
</ul>
<span class="btn btn-outline" style="left:164px;top:1174px;width:158px;height:38px">Message Us</span>
<div class="abs" style="left:686px;top:902px;width:384px;height:356px;background:var(--green);border-radius:0 14px 14px 0"></div>
<div class="abs" role="img" aria-label="Photo of a bearded lawyer with glasses working on a laptop" style="left:668px;top:891px;width:382px;height:350px;background:linear-gradient(150deg,#9fb3c6 0%,#5f7891 45%,#233040 100%);border-radius:0 10px 0 0"></div>
<div class="abs" role="img" aria-label="Laptop on desk" style="left:620px;top:1090px;width:220px;height:110px;background:linear-gradient(160deg,#f2f4f5,#c9ced2);border-radius:6px"></div>

<div class="abs" style="left:170px;top:1500px;width:90px;height:90px;border-radius:50%;background:var(--green)"></div>
<div class="abs" role="img" aria-label="Collage of a law firm member portal screen with photos of lawyers and a handshake" style="left:212px;top:1386px;width:285px;height:372px;background:linear-gradient(180deg,#ffffff,#f1f3f5);box-shadow:0 2px 10px rgba(0,0,0,.12);border-radius:6px"></div>
<div class="abs" role="img" aria-label="Photo of a handshake" style="left:312px;top:1402px;width:178px;height:84px;background:linear-gradient(135deg,#b6a08e,#4d4540)"></div>
<div class="abs" role="img" aria-label="Photo of a smiling businesswoman" style="left:418px;top:1420px;width:152px;height:172px;background:linear-gradient(160deg,#e0e3e6,#8f8279);border-radius:6px;box-shadow:0 2px 8px rgba(0,0,0,.15)"></div>
<div class="abs" style="left:498px;top:1600px;width:42px;height:42px;border-radius:0 0 42px 42px;background:var(--night)"></div>
<div class="abs" role="img" aria-label="Photo of a lawyer reading a document" style="left:135px;top:1550px;width:152px;height:190px;background:linear-gradient(160deg,#c5ccd3,#384452);border-radius:6px;box-shadow:0 2px 8px rgba(0,0,0,.15)"></div>

<h2 class="find-title">Simply find the right lawyer</h2>
<p class="find-text">The industry's standard dummy text ever since the 1500s. when an unknown printer took a galley of type and scrambled it to make a type specimen book. It has survived not.</p>
<ul class="ticks abs" style="left:646px;top:1518px;width:380px">
  <li style="margin-bottom:15px"><svg width="15" height="15" viewBox="0 0 15 15"><circle cx="7.5" cy="7.5" r="7.5" fill="#1b7a2c"/><path d="M4 7.7l2.3 2.3L11 5.3" stroke="#fff" stroke-width="1.6" fill="none"/></svg>The industry's standard dummy text ever since the 1500s. when an unknown.</li>
  <li style="margin-bottom:17px"><svg width="15" height="15" viewBox="0 0 15 15"><circle cx="7.5" cy="7.5" r="7.5" fill="#1b7a2c"/><path d="M4 7.7l2.3 2.3L11 5.3" stroke="#fff" stroke-width="1.6" fill="none"/></svg>The industry's standard dummy text ever since the 1500s. when an unknown.</li>
  <li style="margin-bottom:15px"><svg width="15" height="15" viewBox="0 0 15 15"><circle cx="7.5" cy="7.5" r="7.5" fill="#1b7a2c"/><path d="M4 7.7l2.3 2.3L11 5.3" stroke="#fff" stroke-width="1.6" fill="none"/></svg>The industry's standard dummy text ever since the 1500s. when an unknown.</li>
  <li><svg width="15" height="15" viewBox="0 0 15 15"><circle cx="7.5" cy="7.5" r="7.5" fill="#1b7a2c"/><path d="M4 7.7l2.3 2.3L11 5.3" stroke="#fff" stroke-width="1.6" fill="none"/></svg>The industry's standard dummy text ever since the 1500s. when an unknown.</li>
</ul>
<span class="btn btn-outline" style="left:647px;top:1726px;width:132px;height:33px;font-size:10px">Contact Us Now</span>

<div class="abs" style="left:312px;top:1832px;width:12px;height:12px;border:1.5px solid var(--green);border-radius:50%"></div>
<div class="abs" style="left:852px;top:1805px;width:8px;height:8px;border:1.5px solid var(--green);border-radius:50%"></div>

<section class="steps">
  <h2 class="h2" style="top:56px;line-height:38px">First Steps When Facing<br>A Criminal Charge</h2>
  <div class="abs" style="left:123px;top:228px;width:76px;height:76px;border-radius:50%;background:var(--green)"></div>
  <div class="abs" style="left:1010px;top:350px;width:56px;height:56px;border-radius:50%;border:6px solid var(--night);border-top-color:transparent;border-left-color:transparent"></div>
  <svg class="abs" style="left:420px;top:250px" width="380" height="40"><path d="M0 18 L57 26 M317 16 L380 14" stroke="#9aa" stroke-dasharray="2 3"/></svg>
  <div class="step" style="left:160px">
    <div class="step-icon"><svg width="28" height="28" viewBox="0 0 28 28"><circle cx="12" cy="12" r="8" stroke="#fff" stroke-width="2" fill="none"/><path d="M18 18l7 7" stroke="#fff" stroke-width="2.5"/></svg></div>
    <div class="step-no">STEP 01</div><h3>Analysis &amp; Strategize</h3>
    <p>The industry's standard dummy text ever since the 1500s. when an unknown printer took</p>
  </div>
  <div class="step" style="left:477px">
    <div class="step-icon"><svg width="30" height="30" viewBox="0 0 30 30"><circle cx="9" cy="9" r="4" fill="#fff"/><circle cx="21" cy="9" r="4" fill="#fff"/><path d="M2 24c0-6 3-9 7-9s7 3 7 9zM14 24c0-6 3-9 7-9s7 3 7 9z" fill="#fff"/></svg></div>
    <div class="step-no">STEP 02</div><h3>Negotition</h3>
    <p>The industry's standard dummy text ever since the 1500s. when an unknown printer took</p>
  </div>
  <div class="step" style="left:794px">
    <div class="step-icon"><svg width="30" height="30" viewBox="0 0 30 30"><path d="M15 3v22M6 8h18M9 26h12" stroke="#fff" stroke-width="2"/><path d="M6 8l-4 9h8zM24 8l-4 9h8z" stroke="#fff" stroke-width="1.5" fill="none"/></svg></div>
    <div class="step-no">STEP 03</div><h3>Advocacy at Trial</h3>
    <p>The industry's standard dummy text ever since the 1500s. when an unknown printer took</p>
  </div>
  <span class="btn btn-outline" style="left:527px;top:431px;width:161px;height:36px;font-size:10px">Contact Us Now</span>
</section>

<section class="voices">
  <h2 class="h2" style="top:64px;color:var(--white)">What People Says</h2>
  <div class="voice" style="left:188px"><p>Pellentesque faucibus Ut accumsan ultricies elit Maecenas at justo id velit placerat molestie Donec dictum lectus non</p><strong>Advocate</strong></div>
  <div class="avatar" role="img" aria-label="Portrait photo of client" style="left:361px"></div>
  <div class="voice" style="left:628px"><p>Pellentesque faucibus Ut accumsan ultricies elit Maecenas at justo id velit placerat molestie Donec dictum lectus non</p><strong>Sam</strong></div>
  <div class="avatar" role="img" aria-label="Portrait photo of client" style="left:801px"></div>
  <div class="voice" style="left:1064px;text-align:left;padding-left:54px"><p style="margin:0">Pellentesque faucibus Ut accumsan ultricies elit Maecenas at justo id velit placerat molestie Donec dictum lectus non</p></div>
  <div class="dots" style="left:570px;top:402px"><span></span><span></span><span></span><span></span></div>
</section>

<h2 class="h2" style="top:2893px">Practice Areas</h2>
<section class="practice">
  <article class="area" style="left:93px"><div class="area-photo" role="img" aria-label="Photo of lawyer with handcuffs on a desk" style="background:linear-gradient(135deg,#8a6a55,#3c2d26)"></div><h3>Criminal Law</h3><p>Work encompasses more than mere employment—it's a conduit for growth, identity, and achievement.</p><span class="btn btn-solid">Learn More</span></article>
  <article class="area" style="left:437px"><div class="area-photo" role="img" aria-label="Photo of a family meeting with a lawyer" style="background:linear-gradient(135deg,#d6d2cc,#5a4f52)"></div><h3>Family Law</h3><p>Work encompasses more than mere employment—it's a conduit for growth, identity, and achievement.</p><span class="btn btn-solid">Learn More</span></article>
  <article class="area" style="left:782px"><div class="area-photo" role="img" aria-label="Photo of a justice statue and gavel on a desk" style="background:linear-gradient(135deg,#4e5a68,#201c1a)"></div><h3>Civil Litigation</h3><p>Work encompasses more than mere employment—it's a conduit for growth, identity, and achievement.</p><span class="btn btn-solid">Learn More</span></article>
  <article class="area" style="left:1125px"><div class="area-photo" role="img" aria-label="Photo of clients signing a will" style="background:linear-gradient(135deg,#9fb3cf,#4a5a6e)"></div><h3>Wills &amp; Probate</h3><p>Work encompasses more than mere employment—it's a conduit for growth, identity, and achievement.</p><span class="btn btn-solid">Learn More</span></article>
</section>
<div class="dots" style="left:570px;top:3394px"><span style="background:var(--night)"></span><span style="background:var(--green)"></span><span style="background:var(--night)"></span></div>

<section class="gallery-band">
  <div class="abs" style="left:268px;top:-6px;width:12px;height:12px;border:1.5px solid var(--green);border-radius:50%"></div>
  <div class="abs" style="left:948px;top:-14px;width:8px;height:8px;border:1.5px solid var(--green);border-radius:50%"></div>
  <h2 class="h2" style="top:40px">Featured Gallery</h2>
</section>
<div class="gallery">
  <div role="img" aria-label="Photo of lawyers in discussion" style="background:linear-gradient(135deg,#c9ccd0,#2b3340)"></div>
  <div role="img" aria-label="Photo of a handshake with green overlay" style="background:linear-gradient(135deg,#3a9a45,#1b6a25)">
    <div class="abs" style="left:110px;top:130px;display:flex;gap:16px"><span style="width:18px;height:18px;border-radius:50%;background:#fff"></span><span style="width:18px;height:18px;border-radius:50%;background:#fff"></span><span style="width:18px;height:18px;border-radius:50%;background:#fff"></span></div>
  </div>
  <div role="img" aria-label="Photo of a senior lawyer at a desk" style="background:linear-gradient(135deg,#a99b8f,#2e2a28)"></div>
  <div role="img" aria-label="Photo of colleagues reviewing documents" style="background:linear-gradient(135deg,#eaeaea,#6e7f93)"></div>
</div>

<section class="message">
  <h2>Leave us a Message</h2>
  <div class="field" style="top:97px">Name*</div>
  <div class="field" style="top:159px">Email*</div>
  <div class="field" style="top:220px">Phone</div>
  <div class="field" style="top:281px">Subject</div>
  <div class="field" style="top:343px;height:107px">Message</div>
  <span class="btn" style="left:288px;top:465px;width:145px;height:36px;border:1.5px solid #fff;color:#fff;font-size:10px">Send Message &gt;</span>
</section>

<footer class="footer">
  <svg class="bg" width="1200" height="538" viewBox="0 0 1200 538">
    <polygon points="0,34 255,34 255,0 0,0" fill="#fff"/>
    <polygon points="0,52 255,34 967,34 967,0 1200,0 1200,538 0,538" fill="#197a2b"/>
    <polygon points="0,34 255,34 255,34 0,52" fill="#202020"/>
  </svg>
  <h3 class="news-title">SUSCRIBE OUR NEWSLETTER</h3>
  <div class="news-input">info@yourmail.test</div>
  <span class="btn btn-white news-btn" style="font-size:10px">Suscribe Now</span>

  <div class="f-col" style="left:162px;top:190px;width:250px">
    <div class="brand" style="color:#fff;font-size:20px"><span class="brand-dot" style="background:#fff"></span>GREENVALE LAWYERS</div>
    <p style="margin-top:22px;font-size:11px;line-height:22px;width:230px">The industry's standard dummy text ever since the 1500s. when an unknown printer took a galley.</p>
    <div class="social"><span></span><span></span><span></span></div>
  </div>
  <div class="f-col" style="left:447px">
    <h4>Navigation</h4>
    <ul><li>Home</li><li>About Us</li><li>Lawyers</li><li>Practice Areas</li><li>Contact Us</li></ul>
  </div>
  <div class="f-col" style="left:622px">
    <h4>Contact Us</h4>
    <div class="f-item"><i><svg width="14" height="14" viewBox="0 0 24 24"><path d="M6.6 10.8a15 15 0 006.6 6.6l2.2-2.2c.3-.3.7-.4 1-.2 1.1.4 2.3.6 3.6.6.6 0 1 .4 1 1V20c0 .6-.4 1-1 1A17 17 0 013 4c0-.6.4-1 1-1h3.5c.6 0 1 .4 1 1 0 1.3.2 2.5.6 3.6.1.3 0 .7-.2 1z" fill="#197a2b"/></svg></i>Phone<br>0400 123 45</div>
    <div class="f-item"><i><svg width="14" height="14" viewBox="0 0 24 24"><rect x="3" y="5" width="18" height="14" rx="2" fill="#197a2b"/><path d="M3 7l9 6 9-6" stroke="#fff" stroke-width="1.6" fill="none"/></svg></i>Email<br>hello@greenvalelawyers.com.au</div>
    <div class="f-item"><i><svg width="14" height="14" viewBox="0 0 24 24"><path d="M12 2a7 7 0 00-7 7c0 5 7 13 7 13s7-8 7-13a7 7 0 00-7-7z" fill="#197a2b"/><circle cx="12" cy="9" r="2.5" fill="#fff"/></svg></i>Address<br>88 Harbour Lane, Melbourne VIC 3000</div>
  </div>
  <div class="f-col" style="left:930px">
    <h4>Follow Us</h4>
    <div role="img" aria-label="Map showing the office location in Melbourne" style="width:170px;height:130px;background:linear-gradient(135deg,#e9eef2,#c7d3dd)"></div>
  </div>
  <div class="copyright">© 2023 Greenvale Lawyers. All Rights Reserved</div>
</footer>

</body>
</html>
```